4 x 9 Rack Card Design: Cheer Every Game Advertising Campaign

We would like a 4 x 9 Rack Card Designed using our logo as the basis for the design. We would like to incorporate the images of the shoes & the colors that are on our logo. We are attaching an image of the logo for your use.

The design should use both the front & back of the 4 x 9 card.

All text & fonts should be in "comic sans".

The card should have a fun, youthful, cartoon feel to it.

We would like the following information on the card:
Our logo: See attached file

Our Tag Line: Charity providing Athletic Footwear to Kids

Our Catch Phrase: "Cheer Every Game". Please include small images of various sports balls under, or around or near the catch phrase. Please use images of a Basketball, baseball, golf ball, soccer ball, Hockey Puck, American Football, Tennis ball.

Our Contact Information: PO Box 30628, Phoenix, AZ 85019; phone 480.213.4496; www.brightlace-kids.org; also use the "find us on linkwall" image.

Who we are: We are a 501(c)3 non-profit organization providing athletic footwear to disadvantaged and at-risk youth. The proper footwear allows participation in sports activities providing a healthy outlet for energy, increased self confidence, reduced juvenile crime rates, decline in alcohol, tobacco and drug dependency, strengthened relationships and enhanced academic performance.

A Recipe: We are working on a recipe to be included. In the meantime, we are asking for designs that include a small area for a recipe on the back of the card. The recipe will be easy, with very few ingredients & instructions, so it won't take up too much space on the rack card.

Target Market(s)

Sponsors, endorsers, donators, sports teams.

Industry/Entity Type

Non-Profit

Font styles to use
Other font styles liked:
• Comic Sans

Requirements
Must have
• See project descripion
Nice to have
• See project description. Also, please take a look at our website at www.brightlace-kids.com for our style & additional information about our organization.

```html
<!DOCTYPE html>
<html lang="en">
<head>
<meta charset="utf-8">
<title>Brightlace Kids Rack Card</title>
<link rel="stylesheet" href="https://fonts.googleapis.com/css2?family=Baloo+2:wght@700;800&family=Lato:wght@400;700&family=Roboto+Condensed:wght@700&family=Roboto:wght@400&display=swap">
<style>
  :root {
    --pink: #e8185a;
    --green: #8cc63f;
    --green-light: #b3dc55;
    --green-dark: #6fae2a;
    --blue: #1b95d6;
    --orange: #f07a1b;
    --yellow: #f5cf14;
    --purple: #8a3fb5;
    --ink: #2b2b2b;
    --white: #ffffff;
    --stage: #e4e4e4;
    --rule: #505050;
  }
  * { box-sizing: border-box; margin: 0; padding: 0; }
  html, body { width: 1200px; height: 907px; overflow: hidden; background: var(--stage); }
  .stage { position: relative; width: 1200px; height: 907px; }

  .rack-card {
    position: absolute; top: 37px; width: 382px; height: 834px;
    background: var(--white); overflow: hidden;
    box-shadow: 0 4px 14px rgba(0,0,0,.35);
    font-family: "Lato", sans-serif; color: var(--ink);
  }
  .rack-card--front { left: 181px; }
  .rack-card--back { left: 638px; }
  .card-shapes { position: absolute; inset: 0; width: 382px; height: 834px; }

  .photo { position: absolute; }
  .photo-circle { position: absolute; width: 102px; height: 102px; border-radius: 50%; border: 4px solid var(--pink); }
  .photo-circle--blue { border-color: var(--blue); }

  .logo-art {
    position: absolute; left: 35px; top: 14px; width: 312px; height: 92px;
    background: linear-gradient(90deg, #e8f2fb, #fff2e4, #fffbe0, #eef8e0, #fde6ee);
    border-radius: 8px;
  }
  .logo-name {
    position: absolute; left: 0; right: 0; top: 110px; text-align: center;
    font-family: "Baloo 2", sans-serif; font-weight: 700; font-size: 36px; color: var(--blue); line-height: 1;
  }

  .fun-title { position: absolute; font-family: "Baloo 2", sans-serif; font-weight: 800; line-height: 1; letter-spacing: .5px; }
  .c1 { color: var(--orange); } .c2 { color: var(--pink); } .c3 { color: var(--blue); }
  .c4 { color: var(--yellow); } .c5 { color: var(--purple); } .c6 { color: #e53b2c; }
  .tagline-main { left: 0; right: 0; top: 494px; text-align: center; font-size: 31px; text-shadow: 0 0 3px #fff, 0 0 3px #fff; }
  .tagline-sub {
    position: absolute; left: 0; right: 0; top: 530px; text-align: center;
    font-family: "Roboto", sans-serif; font-size: 20.5px; color: var(--ink);
  }

  .section-label {
    position: absolute; left: 0; height: 24px; padding: 0 14px 0 20px;
    background: var(--pink); color: var(--white); border-radius: 0 12px 12px 0;
    font-family: "Roboto Condensed", sans-serif; font-weight: 700; font-size: 17px; line-height: 24px;
  }
  .about-text {
    position: absolute; left: 21px; top: 610px; width: 160px;
    font-size: 12.6px; line-height: 16.6px; text-align: justify; hyphens: auto;
  }

  .speech-bubble { position: absolute; left: 195px; top: 583px; width: 150px; height: 85px; }
  .speech-text {
    position: absolute; left: 195px; top: 600px; width: 142px; text-align: center;
    font-family: "Roboto Condensed", sans-serif; font-weight: 700; line-height: 19px;
  }
  .speech-text .line1 { color: var(--white); font-size: 16px; display: block; }
  .speech-text .line2 { color: var(--yellow); font-size: 17px; display: block; }

  .character { position: absolute; border-radius: 40px; }

  .bullet-list { position: absolute; left: 23px; list-style: none; font-weight: 700; font-size: 14px; line-height: 17.9px; }
  .bullet-list li { position: relative; padding-left: 12px; }
  .bullet-list li::before {
    content: ""; position: absolute; left: 0; top: 6px; width: 6px; height: 6px; border-radius: 50%; background: var(--orange);
  }

  .contact { position: absolute; color: var(--white); font-size: 12.5px; line-height: 16px; }
  .contact-line { display: flex; align-items: center; gap: 5px; white-space: nowrap; }
  .contact-line svg { width: 9px; height: 9px; flex: none; }
  .social-square { display: inline-block; width: 11px; height: 11px; background: var(--white); border-radius: 2px; margin-left: 4px; }
</style>
</head>
<body>
<main class="stage">

  <!-- Front -->
  <section class="rack-card rack-card--front">
    <div class="photo" style="left:0;top:178px;width:382px;height:290px;background:linear-gradient(160deg,#8fa047 0%,#b39a62 45%,#a57a4c 70%,#7b8a3c 100%)" role="img" aria-label="Young softball player sliding into base"></div>

    <svg class="card-shapes" viewBox="0 0 382 834" aria-hidden="true">
      <defs>
        <radialGradient id="frontGlow" cx="0.5" cy="0.55" r="0.7">
          <stop offset="0" stop-color="#b8df5a"/>
          <stop offset="1" stop-color="#7dbb34"/>
        </radialGradient>
      </defs>
      <path d="M0 0 H382 V184 Q200 176 0 210 Z" fill="#fff"/>
      <path d="M0 210 Q200 176 382 184" fill="none" stroke="var(--rule)" stroke-width="6"/>
      <path d="M0 455 Q190 492 382 446 V834 H0 Z" fill="url(#frontGlow)"/>
      <path d="M0 455 Q190 492 382 446" fill="none" stroke="#fff" stroke-width="7"/>
      <path d="M0 777 Q185 760 250 834 H0 Z" fill="var(--pink)" stroke="#fff" stroke-width="3"/>
    </svg>

    <div class="logo-art" role="img" aria-label="Row of five colourful cartoon sports shoes"></div>
    <div class="logo-name">Brightlace Kids</div>

    <div class="photo-circle" style="left:18px;top:367px;background:linear-gradient(#9cc06a,#5d8c3a)" role="img" aria-label="Child playing golf on green"></div>
    <div class="photo-circle photo-circle--blue" style="left:136px;top:367px;background:linear-gradient(#5f9a3f,#3f6a2a)" role="img" aria-label="Child kicking soccer ball"></div>
    <div class="photo-circle" style="left:254px;top:367px;background:linear-gradient(#7b7f86,#c4a77c)" role="img" aria-label="Close-up of athletic shoe on rock"></div>

    <h1 class="fun-title tagline-main"><span class="c1">C</span><span class="c2">H</span><span class="c3">A</span><span class="c4">R</span><span class="c5">I</span><span class="c6">T</span><span class="c3">Y</span> <span class="c2">P</span><span class="c1">R</span><span class="c5">O</span><span class="c3">V</span><span class="c4">I</span><span class="c6">D</span><span class="c2">I</span><span class="c3">N</span><span class="c1">G</span></h1>
    <p class="tagline-sub">ATHLETIC FOOTWEAR TO KIDS</p>

    <h2 class="section-label" style="top:570px;width:148px">WHO WE ARE</h2>
    <p class="about-text">We are a 501(c)3 non-profit organization providing athletic footwear to disadvantaged and at-risk youth. The proper footwear allows participation in sports activities providing a healthy outlet for energy, increased self confidence.</p>

    <svg class="speech-bubble" viewBox="0 0 150 85" aria-hidden="true">
      <path d="M75 3 C118 3 147 18 147 38 C147 58 118 72 86 73 L84 84 L72 73 C32 72 3 58 3 38 C3 18 32 3 75 3 Z" fill="var(--orange)" stroke="#fff" stroke-width="4"/>
    </svg>
    <p class="speech-text"><span class="line1">CHEER</span><span class="line2">EVERY GAME</span></p>

    <div class="character" style="left:245px;top:663px;width:110px;height:150px;background:radial-gradient(circle at 50% 40%,#6fa6e0,#9ccf5a 75%)" role="img" aria-label="Cartoon boy cheering with raised arms"></div>

    <div class="contact" style="left:10px;top:780px">
      <div class="contact-line"><svg viewBox="0 0 10 10"><path d="M2 1 L4 1 L4.6 3 L3.4 4 Q4.5 6 6 6.6 L7 5.4 L9 6 L9 8 Q5 9 1.5 4.5 Q1 2 2 1Z" fill="#fff"/></svg>480-213-4496</div>
      <div class="contact-line"><svg viewBox="0 0 10 10"><rect x="0.5" y="2" width="9" height="6" fill="#fff"/><path d="M0.5 2 L5 5.5 L9.5 2" fill="none" stroke="#e8185a" stroke-width="1"/></svg>shoes@brightlace-kids.org</div>
      <div class="contact-line"><svg viewBox="0 0 10 10"><circle cx="5" cy="5" r="4.3" fill="#fff"/></svg>www.brightlace-kids.org</div>
    </div>
  </section>

  <!-- Back -->
  <section class="rack-card rack-card--back">
    <div class="photo" style="left:0;top:0;width:382px;height:240px;background:linear-gradient(180deg,#b44d8f 0%,#e8885a 45%,#f7c560 65%,#7ba23a 90%)" role="img" aria-label="Cleated foot resting on a soccer ball at sunset"></div>

    <svg class="card-shapes" viewBox="0 0 382 834" aria-hidden="true">
      <defs>
        <radialGradient id="backGlow" cx="0.5" cy="0.5" r="0.7">
          <stop offset="0" stop-color="#b8df5a"/>
          <stop offset="1" stop-color="#7dbb34"/>
        </radialGradient>
      </defs>
      <path d="M0 232 Q100 200 191 222 T382 205 V834 H0 Z" fill="url(#backGlow)"/>
      <path d="M0 232 Q100 200 191 222 T382 205" fill="none" stroke="#fff" stroke-width="7"/>
      <path d="M0 776 Q191 744 382 776 V834 H0 Z" fill="var(--pink)" stroke="#fff" stroke-width="3"/>
    </svg>

    <div class="photo-circle photo-circle--blue" style="left:26px;top:194px;background:linear-gradient(#8fc45a,#3b6fb0)" role="img" aria-label="Toddler with a ball on grass"></div>
    <div class="photo-circle" style="left:141px;top:194px;background:linear-gradient(#e9e2e6,#d9a8c4)" role="img" aria-label="Little girl tying her shoes"></div>
    <div class="photo-circle photo-circle--blue" style="left:256px;top:194px;background:linear-gradient(#9dc6e8,#6fa23e)" role="img" aria-label="Two girls playing soccer"></div>

    <h2 class="section-label" style="top:323px;width:118px">BENEFITS</h2>
    <ul class="bullet-list" style="top:372px">
      <li>Reduced juvenile crime rates</li>
      <li>Decline in alcohol</li>
      <li>Tobacco and drug dependency</li>
      <li>Strengthened relationships<br>and enhanced academic performance</li>
    </ul>

    <h2 class="section-label" style="top:477px;width:334px">PROVEN MEASURABLE OUTCOMES</h2>
    <ul class="bullet-list" style="top:530px">
      <li>Enhanced academic performance</li>
      <li>Reduced juvenile crime rates</li>
      <li>Improved self esteem</li>
      <li>Decline in tobacco, alcohol &amp; drug use</li>
      <li>Decreased anger &amp; stress</li>
      <li>Decrease in obesity</li>
      <li>Lower teen pregnancy rates</li>
      <li>Higher high school graduation rates</li>
    </ul>

    <p class="fun-title" style="left:20px;top:702px;font-size:23px;text-shadow:0 0 3px #fff,0 0 3px #fff"><span class="c2">C</span><span class="c1">H</span><span class="c3">E</span><span class="c4">E</span><span class="c6">R</span> <span class="c2">E</span><span class="c3">V</span><span class="c1">E</span><span class="c5">R</span><span class="c4">Y</span> <span class="c3">G</span><span class="c2">A</span><span class="c1">M</span><span class="c6">E</span></p>

    <div class="character" style="left:272px;top:650px;width:92px;height:134px;background:radial-gradient(circle at 50% 40%,#f0a35a,#5dbb4a 75%)" role="img" aria-label="Cartoon boy holding a beach ball"></div>

    <div class="contact" style="left:18px;top:786px">
      <div class="contact-line"><svg viewBox="0 0 10 10"><path d="M2 1 L4 1 L4.6 3 L3.4 4 Q4.5 6 6 6.6 L7 5.4 L9 6 L9 8 Q5 9 1.5 4.5 Q1 2 2 1Z" fill="#fff"/></svg>480-213-4496</div>
      <div class="contact-line"><svg viewBox="0 0 10 10"><circle cx="5" cy="5" r="4.3" fill="#fff"/></svg>www.brightlace-kids.org&nbsp;&nbsp;follow us<span class="social-square"></span></div>
    </div>
    <div class="contact" style="left:178px;top:786px">
      <div class="contact-line"><svg viewBox="0 0 10 10"><rect x="0.5" y="2" width="9" height="6" fill="#fff"/><path d="M0.5 2 L5 5.5 L9.5 2" fill="none" stroke="#e8185a" stroke-width="1"/></svg>shoes@brightlace-kids.org</div>
    </div>
  </section>

</main>
</body>
</html>
```